Website incl. html for real estate project

We need the design and implementation of a website for a real estate project. Condominiums are built, which are sold.
We upload the sales brochure. The website should be based on the design of the sales brochure.
There are three houses with 5 apartments each. It should be rendered like this. The structure of the menu should be roughly as follows. Most information about the content is either in the appendix as a picture or in the brochure (PDF)):
Home (page 4-5 from the brochure)
House A
house B
house c
overview
basement
Municipal elections (page 6-7 in the brochure pdf)
Contact
Please use Roboto Regular as font.
And one page should give an overview of all apartments with the prices, the living space, etc. as on the file overview2.jpg.
If you go to the House A, House B, or House C menus, a page should come up with the details for that house only. The pages in the brochure are:
House A (Page 10-11)
House B (page 22-23)
House C (page 34-35)
The individual apartments should each be shown on a property page. There the plan / floor plan of the apartment and the pictures from the inside should be shown. As with the object page.jpg attachment.
Für die Designer... Mehr Zeit...
Coded - Design and coding required
1 page

```html
<!DOCTYPE html>
<html lang="de">
<head>
<meta charset="utf-8">
<title>Wohnpark zur Eiche – Brunnhof Immobilien AG</title>
<link rel="stylesheet" href="https://fonts.googleapis.com/css2?family=Roboto:wght@400;500;700;900&display=swap">
<style>
:root{
  --blue:#1f5f99;
  --red:#e3151d;
  --ink:#222;
  --text:#444;
  --line:#e2e2e2;
  --dark:#121212;
}
*{box-sizing:border-box;margin:0;padding:0}
html,body{width:1200px;height:5286px;overflow:hidden}
body{font-family:'Roboto',sans-serif;color:var(--text);background:#fff;position:relative}
.abs{position:absolute}
.topbar{position:absolute;left:340px;top:0;width:860px;height:34px;background:var(--red);color:#fff;font-size:13px;display:flex;align-items:center}
.topbar .contact{display:flex;gap:26px;margin-left:130px;align-items:center}
.topbar .contact span{display:flex;align-items:center;gap:6px}
.topbar .follow{position:absolute;right:0;top:0;height:34px;width:250px;background:var(--blue);display:flex;align-items:center;gap:8px;padding-left:24px;font-weight:500}
.topbar .follow i{width:10px;height:10px;border-radius:50%;background:#fff;display:inline-block}
.logo{position:absolute;left:100px;top:50px;display:flex;align-items:center;gap:10px;color:var(--blue);font-size:30px;font-weight:700;letter-spacing:1px;line-height:34px}
.logo .mark{width:14px;height:14px;background:var(--red)}
.nav{position:absolute;top:60px;left:366px;display:flex;gap:36px;font-size:13px;font-weight:500;color:var(--ink);text-transform:uppercase}
.hero{position:absolute;left:0;top:102px;width:1200px;height:624px;background:linear-gradient(180deg,#b9c9d8 0%,#dfe5ea 40%,#b6b8b4 55%,#6f8c52 75%,#4e6e34 100%)}
.dots{position:absolute;top:680px;left:554px;display:flex;gap:14px}
.dots i{width:12px;height:12px;border:2px solid #fff;border-radius:50%;display:block}
.dots i.on{background:#fff}
.title{position:absolute;left:0;width:1200px;text-align:center;font-size:36px;font-weight:700;color:var(--ink);letter-spacing:.5px}
.title::before{content:"";display:block;width:56px;height:3px;background:var(--red);margin:0 auto 22px}
.title em{font-style:normal;color:var(--blue)}
.intro{position:absolute;top:904px;font-size:13.5px;line-height:25px}
.intro p{margin-bottom:14px}
.stats{position:absolute;top:1398px;left:100px;display:flex;gap:25px}
.hex{position:relative;width:180px;height:206px;text-align:center}
.hex svg{position:absolute;inset:0}
.hex b{position:relative;display:block;padding-top:48px;font-size:56px;font-weight:500;color:var(--red);line-height:60px}
.hex span{position:relative;display:block;font-size:12px;color:var(--ink);margin-top:10px;line-height:16px}
.ph{position:absolute}
.house-title{position:absolute;font-size:36px;font-weight:700;color:var(--ink)}
.house-title::after{content:"";display:block;width:56px;height:3px;background:var(--red);margin-top:14px}
.desc{position:absolute;font-size:13px;line-height:26px;text-align:justify;width:452px}
.units{position:absolute;background:#fff;border:1px solid var(--line);box-shadow:0 0 8px rgba(0,0,0,.06);font-size:13px;color:var(--ink);border-collapse:collapse}
.units td{padding:9px 14px 9px 30px;border-bottom:1px solid var(--line);vertical-align:top;line-height:16px}
.units tr:last-child td{border-bottom:0}
.redbar{position:absolute;height:14px;background:var(--red)}
.ctitle{position:absolute;left:640px;top:4430px;font-size:38px;font-weight:700;color:var(--ink)}
.ctitle em{font-style:normal;color:var(--blue)}
.field{position:absolute;border:1px solid var(--line);height:42px;font-size:13px;color:var(--ink);padding:14px 14px}
.btn{position:absolute;left:640px;top:4787px;width:162px;height:44px;background:var(--red);color:#fff;font-weight:700;font-size:14px;display:flex;align-items:center;justify-content:center}
.footer{position:absolute;left:0;top:4889px;width:1200px;height:397px;background:var(--dark);color:#ddd;font-size:13px}
.footer h4{font-size:18px;font-weight:500;color:#fff;margin-bottom:22px}
.fcol{position:absolute;top:52px;line-height:27px}
.flogo{position:absolute;left:100px;top:90px;color:#fff;font-size:30px;font-weight:700;letter-spacing:1px;display:flex;gap:10px;align-items:center}
.flogo .mark{width:14px;height:14px;background:var(--red)}
.social{position:absolute;left:154px;top:165px;display:flex;gap:14px}
.social i{width:34px;height:34px;border-radius:50%;background:var(--red);display:block}
.news{position:absolute;left:837px;top:178px;width:264px;height:42px;background:#fff;color:var(--ink);padding:13px 12px}
.news b{position:absolute;right:4px;top:4px;width:34px;height:34px;background:var(--red)}
.copy{position:absolute;left:100px;top:325px;width:1000px;border-top:1px solid #333;text-align:center;padding-top:26px;font-size:13px}
</style>
</head>
<body>

<header>
  <div class="topbar">
    <div class="contact">
      <span><svg width="12" height="12" viewBox="0 0 24 24"><path fill="#fff" d="M6.6 10.8a15 15 0 0 0 6.6 6.6l2.2-2.2c.3-.3.7-.4 1-.2 1.1.4 2.3.6 3.6.6.6 0 1 .4 1 1V20c0 .6-.4 1-1 1A17 17 0 0 1 3 4c0-.6.4-1 1-1h3.5c.6 0 1 .4 1 1 0 1.3.2 2.5.6 3.6.1.3 0 .7-.2 1z"/></svg>+41 61 000 12 34</span>
      <span><svg width="14" height="11" viewBox="0 0 24 18"><rect x="1" y="1" width="22" height="16" fill="none" stroke="#fff" stroke-width="2"/><path d="M1 1l11 9 11-9" fill="none" stroke="#fff" stroke-width="2"/></svg>info@brunnhof-immo.ch</span>
    </div>
    <div class="follow">Follow Us On: <i></i><i></i><i></i></div>
  </div>
  <div class="logo"><span class="mark"></span>BRUNNHOF</div>
  <nav class="nav"><span>Home</span><span>House A</span><span>House B</span><span>House C</span><span>Basement</span><span>Community Elections</span><span>Contact</span></nav>
</header>

<div class="hero" role="img" aria-label="Visualisierung der Wohnanlage mit Haus B und Haus C, Wiese im Vordergrund"></div>
<div class="dots"><i></i><i></i><i class="on"></i><i></i></div>

<section>
  <h2 class="title" style="top:820px">WOHNPARK <em>ZUR EICHE</em></h2>
  <div class="intro" style="left:100px;width:455px">
    <p>Die Überbauung mit drei Mehrfamilienhäusern und insgesamt 15 Eigentumswohnungen entsteht zwischen der Mühlestrasse und dem Rebweg in Birkenau bei Talheim.</p>
    <p>Die modernen und hochwertigen Wohnungen sind gegen das ruhige Quartier Rebmatt und den wunderschönen Ausblick auf den grünen «Hochgrat» ausgerichtet.</p>
    <p>Die Wohnungen befinden sich an idealer Lage in Birkenau mit guter Besonnung und die nächste Bushaltestelle ist nur knapp 120 Meter entfernt. Die Wohnungen sind im Obergeschoss mit grosszügigen Balkon und im Erdgeschoss mit einem gedeckten Sitzplatz und eigenem Garten ausgestattet.</p>
    <p>Der Wohnpark verfügt über ein grosszügiges, gemeinsames Parkhaus, von dem aus in jedes Gebäude ein Lift auf die gewünschte Etage führt. Jede Wohnung verfügt über einen eigenen Keller / ein eigenes Kellerabteil. Zudem ist im Keller ein Schutzraum für die Bewohner vorhanden.</p>
  </div>
  <div class="intro" style="left:623px;width:478px">
    <p>Das Gebäude wird mit 18 bis 30 cm atmungsaktiver Steinwolle isoliert. Geheizt wird über eine moderne Wärmepumpe im Verbund mit einer Photovoltaikanlage, ökologisch hocheffizient mit zeitgemässer Technologie, unabhängig von steigenden Gas und Ölpreisen.</p>
    <p>Alle Wohnungen besitzen einen grosszügigen Wohn-, Koch-/ Essbereich mit raumhohen Fenstern verglast, was für eine helle und freundliche Atmosphäre sorgt.</p>
    <p>Die Umgebungsgestaltung passt perfekt in die ruhige, natürliche und trotzdem moderne Umgebung. Die Grosszügigen Grünflächen der Erdgeschosswohnungen und die dezente Grundbepflanzung verbunden mit den Wegen runden die moderne und zeitlose Architektur des Gebäudes ab.</p>
    <p>Die Wohnungen werden schlüsselfertig zum Fixpreis abgegeben. Es besteht darüber hinaus die Möglichkeit den Innenausbau nach eigenen Wünschen in verschiedenen Bereichen massgeblich mitzugestalten</p>
  </div>
  <div class="stats">
    <div class="hex"><svg viewBox="0 0 180 206"><polygon points="90,3 177,53 177,153 90,203 3,153 3,53" fill="#fff" stroke="#1f5f99" stroke-width="2"/></svg><b>03</b><span>building with individual<br>housing offer</span></div>
    <div class="hex"><svg viewBox="0 0 180 206"><polygon points="90,3 177,53 177,153 90,203 3,153 3,53" fill="#fff" stroke="#1f5f99" stroke-width="2"/></svg><b>09</b><span>Different<br>Floor Plan Types</span></div>
    <div class="hex"><svg viewBox="0 0 180 206"><polygon points="90,3 177,53 177,153 90,203 3,153 3,53" fill="#fff" stroke="#1f5f99" stroke-width="2"/></svg><b>27</b><span>Parking spaces in the<br>underground car park</span></div>
    <div class="hex"><svg viewBox="0 0 180 206"><polygon points="90,3 177,53 177,153 90,203 3,153 3,53" fill="#fff" stroke="#1f5f99" stroke-width="2"/></svg><b>15</b><span>Comfortable<br>Apartments</span></div>
    <div class="hex"><svg viewBox="0 0 180 206"><polygon points="90,3 177,53 177,153 90,203 3,153 3,53" fill="#fff" stroke="#1f5f99" stroke-width="2"/></svg><b>120</b><span>Meters To Bus<br>stop</span></div>
  </div>
</section>

<section>
  <h2 class="title" style="top:1697px">UBERSHICHTSPLAN</h2>
  <div class="ph" style="left:0;top:1780px;width:274px;height:438px;background:linear-gradient(180deg,#dfe3e6,#c9cbc6 55%,#8f9a7c)" role="img" aria-label="Fassadenansicht mit blühendem Baum"></div>
  <div class="ph" style="left:288px;top:1780px;width:625px;height:438px;background:#eef0ea" role="img" aria-label="Situationsplan mit Haus A, Haus B und Haus C"></div>
  <div class="ph" style="left:926px;top:1780px;width:274px;height:438px;background:linear-gradient(180deg,#e8e6e2,#cfcac3 60%,#a9a39b)" role="img" aria-label="Innenansicht Küche und Wohnbereich"></div>
</section>

<section>
  <h2 class="title" style="top:2310px">DIE HAUSER</h2>

  <div class="redbar" style="left:340px;top:2950px;width:228px"></div>
  <div class="ph" style="left:100px;top:2436px;width:455px;height:514px;background:linear-gradient(180deg,#dde3e8,#b8bcbc 45%,#7a7f7a 70%,#5f7a45)" role="img" aria-label="Visualisierung Haus A mit Balkonen und Gärten"></div>
  <h3 class="house-title" style="left:630px;top:2430px">HAUS A</h3>
  <p class="desc" style="left:630px;top:2500px">Das Gebäude «Haus A» verfügt über fünf moderne Wohnungen mit individuellen Grundrissen. Alle Wohnungen haben einen grosszügigen Aussenbereich mit Balkon oder gedecktem Sitzplatz in Richtung Süden zum Hochgrat, dem Birkenauer Hausberg. Die Wohnräume sind mit grossen Fenstern ausgestattet, was die Räume mit Sonnenlicht durchflutet. Das Gebäude ist direkt aus der Tiefgarage mit dem Lift zugänglich</p>
  <table class="units" style="left:425px;top:2728px;width:676px">
    <tr><td>Attika Wohnung</td><td>4.5 Zimmer</td><td>108 m2 Wohnfläche</td><td>105 m2 grosse Sonnenterrasse !</td></tr>
    <tr><td>Obergeschoss</td><td>3.5 Zimmer</td><td>81 m2 Wohnfläche</td><td>16 m2 grosser Balkon</td></tr>
    <tr><td>Obergeschoss</td><td>4.5 Zimmer</td><td>102 m2 Wohnfläche</td><td>33 m2 grosser Balkon</td></tr>
    <tr><td>Erdgeschoss</td><td>3.5 Zimmer</td><td>81 m2 Wohnfläche</td><td>16 m2 gedeckter Sitzplatz und<br>über 120 m² Garten</td></tr>
    <tr><td>Erdgeschoss</td><td>4.5 Zimmer</td><td>102 m2 Wohnfläche</td><td>33 m2 gedeckter Sitzplatz und<br>über 120 m² Garten</td></tr>
  </table>

  <h3 class="house-title" style="left:100px;top:3068px">HAUS B</h3>
  <p class="desc" style="left:100px;top:3138px">Das Gebäude «Haus B» verfügt über fünf moderne Wohnungen mit individuellen Grundrissen. Alle Wohnungen haben einen grosszügigen Balkon oder Terrasse Richtung Süden zum Hochgrat, dem Birkenauer Hausberg, ausgerichtet. Die Wohnräume sind mit grossen Fenstern ausgestattet was die Räume mit hellem Sonnenlicht durchflutet. Das Gebäude ist direkt aus der Tiefgarage mit dem Lift zugänglich.</p>
  <div class="redbar" style="left:633px;top:3578px;width:228px"></div>
  <div class="ph" style="left:644px;top:3078px;width:456px;height:512px;background:linear-gradient(180deg,#dde3e8,#bfc2c1 40%,#7d827c 65%,#5c7a44)" role="img" aria-label="Visualisierung Haus B mit Terrassen"></div>
  <table class="units" style="left:100px;top:3352px;width:676px">
    <tr><td>Attika Wohnung</td><td>4.5 Zimmer</td><td>109 m2 Wohnfläche</td><td>107 m2 grosse Sonnenterrasse !</td></tr>
    <tr><td>Obergeschoss</td><td>2.5 Zimmer</td><td>81 m2 Wohnfläche</td><td>14 m2 grosse Balkon</td></tr>
    <tr><td>Obergeschoss</td><td>4.5 Zimmer</td><td>102 m2 Wohnfläche</td><td>42 m2 grosse Balkon</td></tr>
    <tr><td>Erdgeschoss</td><td>3.5 Zimmer</td><td>81 m2 Wohnfläche</td><td>14 m2 gedeckter Sitzplatz und<br>über 70 m² Garten</td></tr>
    <tr><td>Erdgeschoss</td><td>4.5 Zimmer</td><td>102 m2 Wohnfläche</td><td>42 m2 gedeckter Sitzplatz und<br>über 140 m² Garten</td></tr>
    <tr><td>Untergeschoss</td><td>Hobbyraum</td><td>24 m2 Flächen</td><td>??</td></tr>
  </table>

  <div class="redbar" style="left:340px;top:4213px;width:228px"></div>
  <div class="ph" style="left:100px;top:3715px;width:455px;height:512px;background:linear-gradient(180deg,#dde3e8,#b8bcbc 45%,#7a7f7a 70%,#5f7a45)" role="img" aria-label="Visualisierung Haus C mit Balkonen und Gärten"></div>
  <h3 class="house-title" style="left:630px;top:3710px">HAUS C</h3>
  <p class="desc" style="left:630px;top:3780px">Das Gebäude «Haus C» verfügt über fünf moderne Wohnungen mit individuellen und gross ausgelegten Grundrissen. Alle Wohnungen haben einen grosszügigen Balkon oder Terrasse Richtung Hochgrat, dem Birkenauer Hausberg. Die Wohnräume sind mit grossen Fenstern ausgestattet, was die Räume mit Sonnenlicht durchflutet. Das Gebäude ist direkt aus der Tiefgarage mit dem Lift zugänglich</p>
  <table class="units" style="left:425px;top:4006px;width:676px">
    <tr><td>Attika Wohnung</td><td>4.5 Zimmer</td><td>108 m2 Wohnfläche</td><td>105 m2 grosse Sonnenterrasse !</td></tr>
    <tr><td>Obergeschoss</td><td>3.5 Zimmer</td><td>81 m2 Wohnfläche</td><td>16 m2 grosser Balkon</td></tr>
    <tr><td>Obergeschoss</td><td>4.5 Zimmer</td><td>102 m2 Wohnfläche</td><td>33 m2 grosser Balkon</td></tr>
    <tr><td>Erdgeschoss</td><td>3.5 Zimmer</td><td>81 m2 Wohnfläche</td><td>16 m2 gedeckter Sitzplatz und<br>über 120 m² Garten</td></tr>
    <tr><td>Erdgeschoss</td><td>4.5 Zimmer</td><td>102 m2 Wohnfläche</td><td>33 m2 gedeckter Sitzplatz und<br>über 120 m² Garten</td></tr>
  </table>
</section>

<section>
  <div class="ph" style="left:0;top:4356px;width:592px;height:533px;background:linear-gradient(135deg,#eef0ee,#e4e7e4)" role="img" aria-label="Stadtplan der Umgebung mit Standortmarkierungen"></div>
  <h2 class="ctitle">KONTAKTIERE <em>UNS</em></h2>
  <p class="abs" style="left:640px;top:4488px;width:460px;font-size:14px;line-height:21px;color:var(--ink)">Lorem ipsum dolor sit amet, consectetur adipiscing elit, sed do eiusmod tempor incididunt ut labore</p>
  <div class="field" style="left:640px;top:4542px;width:225px">Name*</div>
  <div class="field" style="left:873px;top:4542px;width:228px">Email*</div>
  <div class="field" style="left:640px;top:4594px;width:225px">Phone*</div>
  <div class="field" style="left:873px;top:4594px;width:228px">Subject*</div>
  <div class="field" style="left:640px;top:4646px;width:461px;height:112px">Message*</div>
  <div class="btn">GET IN TOUCH</div>
</section>

<footer class="footer">
  <div class="flogo"><span class="mark"></span>BRUNNHOF</div>
  <div class="social"><i></i><i></i><i></i></div>
  <div class="fcol" style="left:397px"><h4>Sitemap</h4>Home<br>House A<br>house B<br>house c<br>basement<br>community elections<br>Contact</div>
  <div class="fcol" style="left:600px;width:190px"><h4>Contact info</h4>Brunnhof Immobilien AG Schweiz<br><br>+41 61 000 12 34<br><br>info@brunnhof-immo.ch</div>
  <div class="fcol" style="left:837px;width:264px;line-height:22px"><h4>Sign for newsletter</h4>Sed ut perspiciatis unde omnis iste natus voluptatem</div>
  <div class="news">Email Address<b></b></div>
  <div class="copy">©Copyright ©2022 Brunnhof. All Rights Reserved.</div>
</footer>

</body>
</html>
```